Webpage

I am a professional genealogist. I need a webpage that is professional looking (using the logo I chose), I can add hyperlinks and photos to if and when I want.

```html
<!DOCTYPE html>
<html lang="en">
<head>
<meta charset="utf-8">
<title>Lineage Research Services</title>
<link rel="stylesheet" href="https://fonts.googleapis.com/css2?family=Lustria&family=Open+Sans:wght@300;400;600;700&display=swap">
<style>
:root{
  --teal:#17aebf;
  --teal-soft:#8fd3c0;
  --green:#6fbf98;
  --ink:#222;
  --text:#3a3a3a;
  --heading:#444;
  --rule:#dcdcdc;
  --footer:#f1f1f1;
  --footer-bar:#a8cfe2;
}
*{margin:0;padding:0;box-sizing:border-box}
html,body{width:900px;height:1200px;overflow:hidden;background:#fff}
body{position:relative;font-family:"Open Sans",sans-serif;font-weight:300;color:var(--text)}
.abs{position:absolute}
.serif{font-family:"Lustria",serif;font-weight:400}

/* header */
.brand{left:95px;top:24px;display:flex;align-items:center;gap:12px}
.brand-mark{width:70px;height:70px;border-radius:50%;background:var(--teal-soft)}
.brand-name{font-size:23px;line-height:22px;color:#555;font-weight:300}
.brand-name span{display:block;text-align:right;font-size:17px;color:#888}
.social{top:8px;left:751px;display:flex;gap:4px}
.social i{width:21px;height:21px;border:1.5px solid var(--teal);border-radius:50%;display:block}
.search{left:622px;top:37px;width:177px;height:22px;border:1px solid #bbb;font:italic 11px "Lustria",serif;color:#999;padding:3px 6px}
.search svg{position:absolute;right:5px;top:4px}
.nav{left:410px;top:64px;display:flex;font-size:13.5px;font-weight:400;color:#333}
.nav a{display:block;height:30px;line-height:26px;padding:0 13px;text-decoration:none;color:inherit}
.nav a.active{background:var(--teal);color:#fff}
.topbar{left:0;top:94px;width:900px;height:5px;background:var(--teal)}

/* slider */
.frame{background:#fff;box-shadow:0 0 4px rgba(0,0,0,.3);padding:5px}
.frame div{width:100%;height:100%}
.slide{left:97px;top:135px;width:426px;height:214px;padding:10px}
.slide .photo{background:linear-gradient(135deg,#7a5b3e,#a88560 45%,#3f4f5e)}
.slide-title{left:545px;top:172px;font-size:23px;color:var(--ink)}
.slide-text{left:545px;top:198px;width:260px;font-size:12.3px;line-height:19.5px}
.arrow{top:332px;width:27px;height:28px;display:flex;align-items:center;justify-content:center}
.arrow.prev{left:744px;background:#cfe8dc}
.arrow.next{left:774px;background:var(--green)}
.rule{left:97px;top:370px;width:705px;height:1px;background:var(--rule)}

/* welcome */
.welcome-title{left:95px;top:398px;font-size:25px;color:var(--ink)}
.welcome-text{left:95px;top:436px;width:710px;font-size:12.3px;line-height:19px}

/* services */
.svc-title{width:224px;text-align:center;font-size:19px;line-height:22px;color:var(--heading)}
.svc{width:225px;height:136px}
.g1{background:linear-gradient(135deg,#9b8a76,#5b4c3e)}
.g2{background:linear-gradient(135deg,#e8e8e8,#b9b9b9 60%,#7fa5c7)}
.g3{background:linear-gradient(135deg,#cfe3ee,#8fb7cf 60%,#eef3f6)}
.g4{background:linear-gradient(135deg,#d7dde2,#8a9198 60%,#e4e4e4)}
.g5{background:linear-gradient(135deg,#1a2a5a,#3b7fc0 55%,#a8d1e8)}
.g6{background:linear-gradient(135deg,#a9896b,#d9c2a3 50%,#6f5a45)}

/* about & contact */
.sec-title{font-size:25px;color:var(--ink)}
.about-text{left:95px;top:968px;width:460px;font-size:12.3px;line-height:18.8px}
.contact-text{left:569px;top:968px;width:240px;font-size:12.3px;line-height:18.8px}
.contact-text b{font-weight:700;color:#222}

/* footer */
.footer{left:0;top:1090px;width:900px;height:78px;background:var(--footer)}
.footer-bar{left:0;top:1168px;width:900px;height:32px;background:var(--footer-bar);font-size:10px;color:#fff;padding:10px 0 0 166px;font-weight:400}
.f-brand{left:95px;top:1105px;display:flex;align-items:center;gap:10px}
.f-brand .brand-mark{width:60px;height:60px}
.f-brand .brand-name{font-size:19px;line-height:18px}
.f-brand .brand-name span{font-size:14px}
.f-head{font-size:13px;color:#222}
.f-links{left:350px;top:1120px;display:grid;grid-template-columns:62px 127px 80px;font-size:10.5px;line-height:15.3px;font-weight:400;color:#333}
.news-text{left:636px;top:1119px;font-size:10.5px;font-weight:400;color:#333}
.news-input{left:636px;top:1136px;width:121px;height:22px;border:1px solid #ccc;background:#fff;font:italic 9.5px "Lustria",serif;color:#999;padding:4px 10px}
.news-btn{left:757px;top:1136px;width:43px;height:22px;background:var(--green);color:#fff;font:10.5px "Lustria",serif;text-align:center;line-height:22px}
</style>
</head>
<body>

<header>
  <div class="abs brand"><span class="brand-mark"></span><div class="brand-name">Lineage Research<span>Services</span></div></div>
  <div class="abs social"><i></i><i></i></div>
  <div class="abs search">search...
    <svg width="12" height="12" viewBox="0 0 12 12"><circle cx="5" cy="5" r="3.5" fill="none" stroke="#17aebf" stroke-width="1.6"/><line x1="7.5" y1="7.5" x2="11" y2="11" stroke="#17aebf" stroke-width="2"/></svg>
  </div>
  <nav class="abs nav"><a class="active">Home</a><a>About</a><a>Services</a><a>Publications</a><a>Blog</a><a>Contact</a></nav>
  <div class="abs topbar"></div>
</header>

<section>
  <div class="abs frame slide"><div class="photo" role="img" aria-label="Elderly couple on a sofa holding a framed wedding photograph"></div></div>
  <h2 class="abs serif slide-title">Kinship Determination</h2>
  <p class="abs slide-text">Sed ut perspiciatis unde omnis iste atus error sit voluptatem accusantium doloque laudarat tium, totam rem aperiam, eaque ipsa quae &nbsp;illo inventore veritatis et quasi architecto beatae vitae dicta sunt explicabo.</p>
  <div class="abs arrow prev"><svg width="10" height="18"><polyline points="9,1 1,9 9,17" fill="none" stroke="#fff" stroke-width="1.3"/></svg></div>
  <div class="abs arrow next"><svg width="10" height="18"><polyline points="1,1 9,9 1,17" fill="none" stroke="#fff" stroke-width="1.3"/></svg></div>
  <div class="abs rule"></div>
</section>

<section>
  <h1 class="abs serif welcome-title">Welcome to Lineage Research Services (LRS)</h1>
  <p class="abs welcome-text">Sed ut perspiciatis unde omnis iste natus error sit voluptatem accusantium doloremque laudantium, totam rem aperiam, eaque tas sit aspernatur aut odit aut fugit, sed quia consequuntur magni dolores eos qui ratione voluptatem sequi nesciunt. Neque porro quisquam est, qui dolorem ipsum quia dolor sit amet, consectetur, adip</p>
</section>

<section>
  <h3 class="abs serif svc-title" style="left:95px;top:533px">Forensic Genealogy</h3>
  <h3 class="abs serif svc-title" style="left:335px;top:533px">Kinship Determination</h3>
  <h3 class="abs serif svc-title" style="left:575px;top:519px">Research Analysis<br>and &nbsp;Consultation</h3>
  <div class="abs frame svc" style="left:95px;top:565px"><div class="g1" role="img" aria-label="Vintage sepia family portrait"></div></div>
  <div class="abs frame svc" style="left:335px;top:565px"><div class="g2" role="img" aria-label="Gloved hand holding a test tube over a DNA gel"></div></div>
  <div class="abs frame svc" style="left:575px;top:565px"><div class="g3" role="img" aria-label="Scientists working in a laboratory"></div></div>

  <h3 class="abs serif svc-title" style="left:95px;top:730px">Texas Researcher</h3>
  <h3 class="abs serif svc-title" style="left:335px;top:730px">Record Retrieval</h3>
  <h3 class="abs serif svc-title" style="left:575px;top:728px">More Services</h3>
  <div class="abs frame svc" style="left:95px;top:762px"><div class="g4" role="img" aria-label="Researcher looking through a microscope"></div></div>
  <div class="abs frame svc" style="left:335px;top:762px"><div class="g5" role="img" aria-label="DNA sequence readout on a monitor"></div></div>
  <div class="abs frame svc" style="left:575px;top:762px"><div class="g6" role="img" aria-label="Old photographs with a pocket watch"></div></div>
</section>

<section>
  <h2 class="abs serif sec-title" style="left:97px;top:930px">About Us</h2>
  <p class="abs about-text">Sed ut perspiciatis unde omnis iste natus error sit voluptatem accusantium dolo-remque laudantium, totam rem aperiam, eaque tas sit aspernatur aut odit aut fugit, sed quia consequuntur magni dolores eos qui ratione voluptatem sequi nesciunt. Neque porro quisquam est, qui dolorem ipsum quia doadip.</p>
  <h2 class="abs serif sec-title" style="left:569px;top:930px">Contact</h2>
  <p class="abs contact-text"><b>Dana Whitfield,</b> Professional Genealogist<br><b>address:</b> PO Box 5521 Maple Falls, TX<br><b>phone:</b> 55501-0148 &nbsp;&nbsp;&nbsp;<b>cel:</b> 555-214-0199<br><b>email:</b> dwhitfield@example.net</p>
</section>

<footer>
  <div class="abs footer"></div>
  <div class="abs f-brand"><span class="brand-mark"></span><div class="brand-name">Lineage Research<span>Services</span></div></div>
  <h4 class="abs serif f-head" style="left:350px;top:1098px">Links and Pages</h4>
  <div class="abs f-links"><span>Home</span><span>Terms and Conditions</span><span>Services</span><span>About</span><span>Publications</span><span>Privacy Policy</span><span>Contact</span><span>Blog</span><span>FAQ</span></div>
  <h4 class="abs serif f-head" style="left:637px;top:1098px">News letter</h4>
  <p class="abs news-text">Lorem ipsum dolor set</p>
  <div class="abs news-input">Enter your email</div>
  <div class="abs news-btn">Send</div>
  <div class="abs footer-bar">© 2014 LRS. All Right Reserved</div>
</footer>

</body>
</html>
```